TRELLWICK Construction Group business card for distribution

A business card detailing our services, with our phone number and email address.
- Groundworks / Foundations / Drainage
- Landscaping / Hard Landscaping / Patios / Decking
- Fencing
The card should include company logo and be in the same colours.

Target Market(s)
Domestic Houses
Industry/Entity Type
Construction
Contact Information for Business Card
Phone Number - 07931 258 904 / 07713829516. Email address: trellgroup@stonevane-mail.com
Font styles to use
Serif
Sans Serif
Colors
F0912C
F2A743
F7CA91
FBE8D2
FDF5EE
Requirements
Must have
- Contact numbers. Photos of past work. Company Logo

Nice to have
- Company Logo

```html
<!DOCTYPE html>
<html lang="en">
<head>
<meta charset="utf-8">
<title>TRELLWICK Construction Group – Business Card</title>
<link rel="stylesheet" href="https://fonts.googleapis.com/css2?family=Montserrat:wght@400;600;700&display=swap">
<style>
  :root {
    --backdrop: #1a1a1a;
    --card: #272525;
    --orange: #f0912c;
    --white: #f4f4f4;
    --grey: #c9c9c9;
  }
  * { box-sizing: border-box; margin: 0; padding: 0; }
  html, body {
    width: 1200px; height: 866px; overflow: hidden;
    background: var(--backdrop);
    font-family: "Montserrat", sans-serif;
  }
  .sheet {
    position: relative; width: 1200px; height: 866px;
    display: flex; flex-direction: column; align-items: center; justify-content: center; gap: 44px;
  }
  .card {
    position: relative; width: 660px; height: 377px;
    background: var(--card);
    box-shadow: 0 10px 28px rgba(0,0,0,.55);
    overflow: hidden;
  }
  .brand {
    position: absolute; display: flex; flex-direction: column; align-items: flex-start;
    color: var(--white);
  }
  .brand-row { display: flex; align-items: center; gap: 14px; }
  .brand-name {
    font-weight: 700; letter-spacing: 2px; color: var(--white);
  }
  .brand-mark { background: var(--orange); flex: none; }
  .brand-sub {
    font-weight: 600; letter-spacing: 3px; color: var(--white);
  }
  /* front */
  .card--front .brand { left: 50%; top: 50%; transform: translate(-50%, -50%); }
  .card--front .brand-name { font-size: 64px; line-height: 1; }
  .card--front .brand-mark { width: 40px; height: 40px; }
  .card--front .brand-sub { font-size: 19px; margin-top: 10px; }
  /* back */
  .card--back .brand { right: 40px; top: 44px; }
  .card--back .brand-name { font-size: 44px; line-height: 1; }
  .card--back .brand-mark { width: 28px; height: 28px; }
  .card--back .brand-sub { font-size: 13px; margin-top: 8px; letter-spacing: 2.4px; }
  .services {
    position: absolute; left: 40px; top: 160px; list-style: none;
    font-size: 14px; font-weight: 400; letter-spacing: 1px; color: var(--white);
    line-height: 1.75; text-transform: uppercase;
  }
  .services li::before {
    content: ""; display: inline-block; width: 7px; height: 7px;
    background: var(--orange); margin-right: 8px; vertical-align: 2px;
  }
  .services .sep {
    display: inline-block; width: 7px; height: 7px; background: var(--orange);
    margin: 0 7px; vertical-align: 2px;
  }
  .rule {
    position: absolute; left: 40px; right: 40px; top: 276px; height: 1px; background: var(--orange);
  }
  .contact {
    position: absolute; left: 40px; right: 40px; top: 296px;
    display: flex; justify-content: space-between; align-items: center;
    font-size: 15px; color: var(--white); letter-spacing: .6px;
  }
  .contact-item { display: flex; align-items: center; gap: 9px; }
  .contact-icon { width: 22px; height: 22px; flex: none; }
</style>
</head>
<body>
<main class="sheet">

  <section class="card card--front" aria-label="Card front">
    <div class="brand">
      <div class="brand-row">
        <span class="brand-name">TRELLWICK</span>
        <span class="brand-mark"></span>
      </div>
      <span class="brand-sub">CONSTRUCTION GROUP LTD</span>
    </div>
  </section>

  <section class="card card--back" aria-label="Card back">
    <div class="brand">
      <div class="brand-row">
        <span class="brand-name">TRELLWICK</span>
        <span class="brand-mark"></span>
      </div>
      <span class="brand-sub">CONSTRUCTION GROUP LTD</span>
    </div>

    <ul class="services">
      <li>Groundworks<span class="sep"></span>Foundations<span class="sep"></span>Drainage</li>
      <li>Landscaping<span class="sep"></span>Hard Landscaping<span class="sep"></span>Patios<span class="sep"></span>Decking</li>
      <li>Fencing</li>
    </ul>

    <div class="rule"></div>

    <div class="contact">
      <div class="contact-item">
        <svg class="contact-icon" viewBox="0 0 22 22" aria-hidden="true">
          <circle cx="11" cy="11" r="11" fill="#f0912c"/>
          <path d="M8 6.5c.6-.4 1.2-.3 1.5.3l.8 1.6c.2.5 0 1-.4 1.3l-.5.4c.5 1.2 1.4 2.1 2.6 2.6l.4-.5c.3-.4.8-.6 1.3-.4l1.6.8c.6.3.7.9.3 1.5-.7 1-1.8 1.4-3 .9-2.3-1-4-2.7-5-5-.5-1.2-.1-2.3.4-3.5z" fill="#272525"/>
        </svg>
        <span>07931 258 904 / 07713829516</span>
      </div>
      <div class="contact-item">
        <svg class="contact-icon" viewBox="0 0 22 22" aria-hidden="true">
          <circle cx="11" cy="11" r="11" fill="#f0912c"/>
          <rect x="5.5" y="7" width="11" height="8" fill="#272525"/>
          <path d="M5.5 7l5.5 4.5L16.5 7" fill="none" stroke="#f0912c" stroke-width="1"/>
        </svg>
        <span>trellgroup@stonevane-mail.com</span>
      </div>
    </div>
  </section>

</main>
</body>
</html>
```